" Atendimento em clínica especializada de otorrino na região do Ipiranga (São Paulo - SP), prestando atendimento médico, realizando exames e cirurgias na área. "

```html
<!DOCTYPE html>
<html lang="pt-BR">
<head>
<meta charset="utf-8">
<title>Papel timbrado – Dr. Marcelo Tavares</title>
<link rel="stylesheet" href="https://fonts.googleapis.com/css2?family=Montserrat:wght@400;600;700&family=Open+Sans:wght@400;600&display=swap">
<style>
  :root {
    --bg: #e9e5df;
    --paper: #ffffff;
    --teal: #1a9bc0;
    --teal-dark: #157f9f;
    --ink: #4a4f55;
    --muted: #8a9096;
    --faint: #f1f3f4;
  }
  * { box-sizing: border-box; margin: 0; padding: 0; }
  html, body { width: 1200px; height: 1200px; overflow: hidden; }
  body {
    background: var(--bg);
    font-family: "Open Sans", Arial, sans-serif;
    color: var(--ink);
    display: flex; align-items: center; justify-content: center;
  }
  .letterhead {
    position: relative;
    width: 778px; height: 1100px;
    background: var(--paper);
    box-shadow: 0 6px 24px rgba(0,0,0,.12);
    overflow: hidden;
  }
  .brand {
    position: absolute; top: 64px; right: 70px;
    display: flex; align-items: center; gap: 14px;
  }
  .brand-dot { width: 38px; height: 38px; border-radius: 50%; background: var(--teal); }
  .brand-name {
    font-family: "Montserrat", Arial, sans-serif;
    font-weight: 700; font-size: 26px; letter-spacing: .5px;
    color: var(--teal); text-transform: uppercase; line-height: 1;
  }
  .brand-tagline {
    font-family: "Montserrat", Arial, sans-serif;
    font-size: 11px; letter-spacing: 3px; text-transform: uppercase;
    color: var(--teal); margin-top: 6px;
  }
  .backdrop-mark {
    position: absolute; top: 330px; left: 250px;
    width: 340px; height: 340px; border-radius: 50%;
    background: var(--faint);
  }
  .contacts {
    position: absolute; left: 50px; top: 470px; width: 200px;
    list-style: none; display: flex; flex-direction: column; gap: 14px;
  }
  .contacts li {
    display: flex; align-items: center; gap: 9px;
    font-size: 11.5px; line-height: 1.4; color: var(--muted);
  }
  .contacts svg { width: 22px; height: 22px; flex: none; }
  .letter-body {
    position: absolute; left: 280px; right: 70px; top: 190px;
    font-size: 14px; line-height: 1.75; text-align: justify;
  }
  .letter-body p { margin-bottom: 18px; }
  .sign-off { margin-top: 30px; }
  .signature {
    width: 170px; height: 54px; margin: 10px 0 6px;
    background: linear-gradient(90deg, #d9dcdf, #eef0f1);
    border-radius: 4px;
  }
  .signer { font-family: "Montserrat", Arial, sans-serif; font-weight: 600; font-size: 13px; color: var(--ink); }
  .signer-role { font-size: 11px; color: var(--muted); }
  .footer-bands { position: absolute; left: 0; bottom: 0; width: 778px; height: 90px; }
</style>
</head>
<body>
  <main class="letterhead">
    <header class="brand">
      <span class="brand-dot"></span>
      <div class="brand-text">
        <div class="brand-name">Dr. Marcelo Tavares</div>
        <div class="brand-tagline">Otorrinolaringologia</div>
      </div>
    </header>

    <div class="backdrop-mark" aria-hidden="true"></div>

    <ul class="contacts">
      <li>
        <svg viewBox="0 0 24 24"><circle cx="12" cy="12" r="12" fill="var(--teal)"/><path d="M9 6.5l1.6 2.6-1.2 1.2a7 7 0 0 0 4.3 4.3l1.2-1.2 2.6 1.6-.8 2.2c-4.8.4-9.9-4.7-9.5-9.5z" fill="#fff"/></svg>
        (11) 3000-0000
      </li>
      <li>
        <svg viewBox="0 0 24 24"><circle cx="12" cy="12" r="12" fill="var(--teal)"/><rect x="6" y="8" width="12" height="8" rx="1" fill="#fff"/><path d="M6.5 8.5l5.5 4 5.5-4" stroke="var(--teal)" stroke-width="1.2" fill="none"/></svg>
        contato@tavares.med.br
      </li>
      <li>
        <svg viewBox="0 0 24 24"><circle cx="12" cy="12" r="12" fill="var(--teal)"/><circle cx="12" cy="12" r="6" stroke="#fff" stroke-width="1.4" fill="none"/><path d="M6 12h12M12 6c-2.5 3-2.5 9 0 12M12 6c2.5 3 2.5 9 0 12" stroke="#fff" stroke-width="1.2" fill="none"/></svg>
        www.tavares.med.br
      </li>
      <li>
        <svg viewBox="0 0 24 24"><circle cx="12" cy="12" r="12" fill="var(--teal)"/><path d="M12 5a4.5 4.5 0 0 0-4.5 4.5C7.5 13 12 19 12 19s4.5-6 4.5-9.5A4.5 4.5 0 0 0 12 5z" fill="#fff"/><circle cx="12" cy="9.6" r="1.6" fill="var(--teal)"/></svg>
        <span>Rua das Acácias, 120<br>Ipiranga – São Paulo</span>
      </li>
    </ul>

    <section class="letter-body">
      <p>Prezado paciente, agradecemos a confiança em nossa clínica. Nossa equipe realiza consultas, exames e cirurgias de ouvido, nariz e garganta com cuidado e atenção em cada etapa do atendimento.</p>
      <p>Informamos que os resultados dos seus exames já estão disponíveis. Solicitamos que agende um retorno para que possamos avaliar os resultados juntos e definir os próximos passos do tratamento indicado.</p>
      <p>Lembramos que o acompanhamento regular é essencial para a saúde auditiva e respiratória de toda a família.</p>
      <p>Em caso de dúvidas, nossa recepção está à disposição de segunda a sábado pelos contatos ao lado.</p>
      <div class="sign-off">
        <div>Atenciosamente,</div>
        <div class="signature" role="img" aria-label="Assinatura manuscrita do médico"></div>
        <div class="signer">Dr. Marcelo Tavares</div>
        <div class="signer-role">Otorrinolaringologista</div>
      </div>
    </section>

    <svg class="footer-bands" viewBox="0 0 778 90" aria-hidden="true">
      <path d="M0 22 H400 Q420 22 426 34 H0 Z" fill="var(--teal)"/>
      <path d="M0 58 H470 Q500 58 510 90 H0 Z" fill="var(--teal-dark)"/>
    </svg>
  </main>
</body>
</html>
```